Young Accounting firm needing a captivating business card

We need a business card design that forces the person to look at the card because its either gold foil, plastic, or lettering pop up etc. We already have a logo with a specific gold color and we need to make it pop. We are an accounting firm. I need the words" accounting, payroll, licenses, audits, taxes" somewhere on the business card so as to describe what we do- preferably on the side where the logo is at.

Industry/Entity Type

Accounting

Contact Information for Business Card

Address 48276 9th Ave S Ste 305, Federal Way, WA 98117
Business Phone (360)418-2096
Fax (360)418-2157
Office Cell Phone (360)586-7319

Font styles to use
Serif

Colors
85abd2

Requirements
Must have
• It should state
• "Accounting" "Taxes" "Audits" "Licenses" "Payroll"
Nice to have
• Matte with gold foil, different textures, With Either a textured ivory background or gray blue slate background
Should not have
• colorful colors

```html
<!DOCTYPE html>
<html lang="en">
<head>
<meta charset="utf-8">
<title>Kestrel Ledger — Business Card</title>
<link rel="stylesheet" href="https://fonts.googleapis.com/css2?family=Arimo:wght@700&display=swap">
<style>
  :root {
    --backdrop: #5b5d61;
    --amber-light: #fcc24a;
    --amber-deep: #f0a422;
    --ink: #4a4847;
    --espresso-light: #2e2320;
    --espresso-deep: #1a1211;
    --gold: #d8bd3c;
    --rule-gold: #d9b75a;
  }
  * { box-sizing: border-box; margin: 0; padding: 0; }
  html, body { width: 1200px; height: 900px; overflow: hidden; }
  body {
    background: var(--backdrop);
    font-family: "Arimo", Arial, sans-serif;
    font-weight: 700;
    position: relative;
  }
  .card {
    position: absolute;
    width: 620px;
    height: 354px;
    overflow: hidden;
    box-shadow: 0 10px 24px rgba(0,0,0,0.35);
  }
  .card-texture { position: absolute; inset: 0; }

  /* Front: contact side */
  .card-front { left: 60px; top: 60px; }
  .card-front .card-texture {
    background: linear-gradient(135deg, var(--amber-light) 0%, var(--amber-deep) 55%, var(--amber-light) 100%);
  }
  .front-brand {
    position: absolute;
    left: 44px;
    top: 172px;
    display: flex;
    align-items: center;
    gap: 10px;
    color: var(--ink);
    font-size: 30px;
    letter-spacing: -0.5px;
  }
  .brand-dot {
    width: 16px; height: 16px;
    border-radius: 50%;
    background: currentColor;
  }
  .front-divider {
    position: absolute;
    left: 318px;
    top: 86px;
    width: 2px;
    height: 150px;
    background: var(--rule-gold);
  }
  .contact-list {
    position: absolute;
    left: 346px;
    top: 88px;
    list-style: none;
    color: var(--ink);
    font-size: 17px;
  }
  .contact-list li {
    display: flex;
    align-items: center;
    gap: 14px;
    height: 34px;
  }
  .contact-list svg { width: 18px; height: 18px; flex: none; }
  .front-address {
    position: absolute;
    left: 0; right: 0;
    bottom: 40px;
    text-align: center;
    color: var(--ink);
    font-size: 17px;
  }

  /* Back: brand side */
  .card-back { left: 520px; top: 486px; }
  .card-back .card-texture {
    background: linear-gradient(135deg, var(--espresso-light) 0%, var(--espresso-deep) 50%, var(--espresso-light) 100%);
  }
  .back-brand {
    position: absolute;
    left: 0; right: 0;
    top: 120px;
    display: flex;
    justify-content: center;
    align-items: center;
    gap: 14px;
    color: var(--gold);
    font-size: 50px;
    letter-spacing: -1px;
  }
  .back-brand .brand-dot { width: 24px; height: 24px; }
  .service-list {
    position: absolute;
    left: 0; right: 0;
    bottom: 52px;
    display: flex;
    justify-content: center;
    align-items: center;
    list-style: none;
    color: var(--gold);
    font-size: 17px;
    letter-spacing: 0.5px;
  }
  .service-list li { display: flex; align-items: center; }
  .service-list li + li::before {
    content: "";
    width: 6px; height: 6px;
    border-radius: 50%;
    background: var(--gold);
    margin: 0 12px;
  }
</style>
</head>
<body>

<section class="card card-front">
  <div class="card-texture" role="img" aria-label="Embossed amber diamond quilted pattern"></div>
  <div class="front-brand"><span class="brand-dot"></span>Kestrel Ledger</div>
  <div class="front-divider"></div>
  <ul class="contact-list">
    <li>
      <svg viewBox="0 0 24 24" aria-hidden="true"><path fill="#4a4847" d="M3 9c0-3 4-5 9-5s9 2 9 5v2h-5V9H8v2H3zM6 12h12l2 7H4z"/></svg>
      (360)418-2096
    </li>
    <li>
      <svg viewBox="0 0 24 24" aria-hidden="true"><path fill="none" stroke="#4a4847" stroke-width="2" d="M7 3h8l2 2v5H7zM4 10h16v10H4zM8 14h8"/></svg>
      (360)418-2157
    </li>
    <li>
      <svg viewBox="0 0 24 24" aria-hidden="true"><rect x="7" y="2" width="10" height="20" rx="2" fill="#4a4847"/><rect x="9" y="5" width="6" height="7" fill="#fcc24a"/></svg>
      (360)586-7319
    </li>
    <li>
      <svg viewBox="0 0 24 24" aria-hidden="true"><path fill="#4a4847" d="M2 5h20v14H2z"/><path fill="none" stroke="#fcc24a" stroke-width="1.5" d="M2 5l10 8 10-8"/></svg>
      office@kestrelledger.com
    </li>
  </ul>
  <p class="front-address">48276 9th Ave S Ste 305, Federal Way, WA 98117</p>
</section>

<section class="card card-back">
  <div class="card-texture" role="img" aria-label="Embossed dark espresso diamond quilted pattern"></div>
  <div class="back-brand"><span class="brand-dot"></span>Kestrel Ledger</div>
  <ul class="service-list">
    <li>ACCOUNTING</li>
    <li>TAXES</li>
    <li>AUDITS</li>
    <li>LICENSES</li>
    <li>PAYROLL</li>
  </ul>
</section>

</body>
</html>
```